Varnath Consulting Business card design.

See our website www.varnathconsulting-example.com which will give you a good idea of what we are about. The font is called 'Play'.

I'd like a standout business card in keeping with the themes and branding on the website

Target Market(s)

professionals. HR directors

Industry/Entity Type

Business

Contact Information for Business Card

Varnath Consulting PO Box 3917 Tindale Creek NSW 2840 1300 457 318 Gerald Ashbury Principal email: jobs@varnathconsulting-example.com ABN: 31792048663

Font styles to use
Other font styles liked:
• Play

Requirements
Must have
• Must have same design colours and branding as website.
• On back I'd prefer a list of the things we do which appears below the name at the header on the website

```html
<!DOCTYPE html>
<html lang="en">
<head>
<meta charset="utf-8">
<title>Varnath Consulting Business Card</title>
<link rel="stylesheet" href="https://fonts.googleapis.com/css2?family=Play:wght@400;700&display=swap">
<style>
  :root {
    --navy: #0b1d2f;
    --blue: #3a90d2;
    --sky-top: #1f5fa8;
    --sky-bottom: #3b8fd4;
    --white: #ffffff;
    --page: #eeeeec;
  }
  * { box-sizing: border-box; margin: 0; padding: 0; }
  html, body { width: 1189px; height: 1200px; overflow: hidden; }
  body {
    background: var(--page);
    font-family: 'Play', sans-serif;
    color: var(--white);
    position: relative;
  }
  .card {
    position: absolute;
    left: 171px;
    width: 856px;
    height: 487px;
    background: var(--navy);
    box-shadow: 4px 8px 14px rgba(0,0,0,0.35);
    overflow: hidden;
  }
  .card--front { top: 68px; }
  .card--back { top: 627px; }
  .abs { position: absolute; white-space: nowrap; }

  /* Front */
  .brand-stack { left: 39px; top: 34px; font-size: 62px; font-weight: 700; line-height: 68px; letter-spacing: 1px; }
  .brand-stack .accent { color: var(--blue); display: block; }
  .person { right: 36px; top: 38px; text-align: right; }
  .person__name { font-size: 36px; font-weight: 700; line-height: 40px; letter-spacing: 0.5px; }
  .person__title { font-size: 23px; color: var(--blue); line-height: 26px; }
  .phone { right: 36px; top: 126px; display: flex; align-items: center; gap: 12px; font-size: 24px; }
  .phone__icon { width: 26px; height: 26px; background: var(--blue); display: flex; align-items: center; justify-content: center; }
  .divider { left: 0; width: 100%; height: 9px; background: var(--white); }
  .photo {
    left: 0; top: 192px; width: 100%; height: 214px;
    background: linear-gradient(180deg, var(--sky-top) 0%, var(--sky-bottom) 70%, #c9d9ea 100%);
  }
  .contact-band {
    left: 0; top: 415px; width: 100%; height: 72px;
    background: var(--blue);
    display: flex; align-items: center; justify-content: space-between;
    padding: 0 36px 0 37px; font-size: 20px;
  }
  .contact-item { display: flex; align-items: center; gap: 9px; }
  .contact-icon { width: 26px; height: 26px; background: var(--white); display: flex; align-items: center; justify-content: center; }

  /* Back */
  .brand-line { left: 31px; top: 68px; font-size: 62px; font-weight: 700; letter-spacing: 1px; }
  .brand-line .accent { color: var(--blue); }
  .services { top: 216px; list-style: none; font-size: 24px; line-height: 34px; letter-spacing: 0.3px; }
  .services--left { left: 34px; }
  .services--right { left: 486px; }
  .services li { display: flex; align-items: center; gap: 12px; }
  .services li::before { content: ""; width: 10px; height: 10px; border-radius: 50%; background: var(--blue); flex: none; }
  .address { left: 34px; top: 384px; font-size: 24px; line-height: 34px; font-weight: 700; }
  .abn { left: 486px; top: 418px; font-size: 24px; line-height: 34px; font-weight: 700; }
  .abn .label { color: var(--blue); }
</style>
</head>
<body>

<section class="card card--front">
  <div class="abs brand-stack">VARNATH<span class="accent">CONSULTING</span></div>
  <div class="abs person">
    <div class="person__name">Gerald Ashbury</div>
    <div class="person__title">Managing Director/Principal</div>
  </div>
  <div class="abs phone">
    <span>1300 457 318</span>
    <span class="phone__icon">
      <svg width="16" height="18" viewBox="0 0 16 18"><path d="M4 1 L7 5 L5 7 Q6 11 9 13 L11 11 L15 14 L13 17 Q3 15 1 4 Z" fill="#ffffff"/></svg>
    </span>
  </div>
  <div class="abs divider" style="top:183px"></div>
  <div class="abs photo" role="img" aria-label="Snowboarder mid-jump above a snowy mountain peak against a deep blue sky"></div>
  <div class="abs divider" style="top:406px"></div>
  <div class="abs contact-band">
    <div class="contact-item">
      <span class="contact-icon">
        <svg width="20" height="14" viewBox="0 0 20 14"><rect x="0.5" y="0.5" width="19" height="13" fill="none" stroke="#3a90d2"/><path d="M0.5 0.5 L10 8 L19.5 0.5" fill="none" stroke="#3a90d2"/></svg>
      </span>
      <span>jobs@varnathconsulting-example.com</span>
    </div>
    <div class="contact-item">
      <span class="contact-icon">
        <svg width="20" height="20" viewBox="0 0 20 20" fill="none" stroke="#3a90d2" stroke-width="1.2"><circle cx="10" cy="10" r="8.5"/><ellipse cx="10" cy="10" rx="4" ry="8.5"/><path d="M1.5 10 H18.5 M3 5.5 H17 M3 14.5 H17"/></svg>
      </span>
      <span>www.varnathconsulting-example.com</span>
    </div>
  </div>
</section>

<section class="card card--back">
  <div class="abs brand-line">VARNATH <span class="accent">CONSULTING</span></div>
  <ul class="abs services services--left">
    <li>Search &amp; Selection</li>
    <li>Career Coaching</li>
    <li>Talent Assessment</li>
    <li>Resume Enhancement</li>
  </ul>
  <ul class="abs services services--right">
    <li>Interview Coaching</li>
    <li>Leadership Development</li>
    <li>Personal Development Plans</li>
    <li>Outplacement</li>
  </ul>
  <div class="abs address">PO Box 3917<br>Tindale Creek NSW 2840</div>
  <div class="abs abn"><span class="label">ABN</span> 31792048663</div>
</section>

</body>
</html>
```